Stationery and Logo Design Project for new NZ Accounting Firm

Our company name is based in Auckland, New Zealand and is called TMV CA Limited. We are a chartered accountancy firm hence the CA abbreviations.

We need a full logo stationery design: Logo, Letterhead, Business Card and Compliments slip.

We are looking for a bold, modern and clean/simple design that makes us stand out. We want to stand out as professionals in the industry and would like the logo and stationery that our clients see to convey this image. We also want to break away from the traditional boring views of book/bean accountants. We are not doing the same old things others are doing and are mainly cloud based but with face to face business relationship focused as well.

We see ourselves as business advisers that provide more than just filing their tax returns. We want to add value to their business and be a partner in their business ventures.

We want the logo to convey the above and also attract potential clients when they see our ads among the thousands on zarvo and the tallow index.

The logo can be for the "TMV" with CA Ltd seperately or a logo/design beside the TMV. But open to other suggestions or concept.

Hi Designers

The designs I have received so far is not quite what I want.

I want something modern and bold that is DIFFERENT from others, from the usual logo designs. Some logo that when people look at it they will remember it as opposed to fading in the background of other competitors' logo.

Lower case lettering for the TMV could be something to explore as I have not seen a lot of these and they do appeal to me.

Thanks

We can focus on the logo first as that will form the main part for all stationery.

Reason: Final stages of choosing a logo design so need to time for designers to submit the letterhead, namecards designs.

Target Market(s)

Our target clients are small to medium business ranging from the sole trader to 50 employees businesses

Industry/Entity Type

Business

```html
<!DOCTYPE html>
<html lang="en">
<head>
<meta charset="utf-8">
<title>TMV CA Ltd. – Business Card</title>
<link href="https://fonts.googleapis.com/css2?family=Open+Sans:wght@400;600;700&display=swap" rel="stylesheet">
<style>
  :root {
    --stage: #1b1b1d;
    --blue-deep: #1f4f8c;
    --blue-mid: #2a6fa6;
    --blue-light: #3fb3d3;
    --red: #c8202f;
    --ink: #2a2a2a;
    --rule: #6a6a6a;
    --paper: #f4f4f4;
    --paper-shade: #dcdcdc;
    --white: #ffffff;
  }
  * { margin: 0; padding: 0; box-sizing: border-box; }
  html, body { width: 1200px; height: 900px; overflow: hidden; }
  body {
    background: var(--stage);
    font-family: "Open Sans", Arial, sans-serif;
    position: relative;
  }

  .card {
    position: absolute;
    width: 560px;
    height: 320px;
    border-radius: 3px;
    overflow: hidden;
  }

  /* Back of card */
  .card-back {
    left: 90px;
    top: 70px;
    background: radial-gradient(ellipse at 45% 35%, var(--blue-light) 0%, var(--blue-mid) 45%, var(--blue-deep) 100%);
  }
  .card-back .wordmark {
    position: absolute;
    left: 0; right: 0;
    top: 108px;
    text-align: center;
    color: var(--white);
    font-weight: 700;
    font-size: 52px;
    letter-spacing: 1px;
  }
  .card-back .web {
    position: absolute;
    left: 0; right: 0;
    bottom: 44px;
    text-align: center;
    color: var(--white);
    font-size: 15px;
    letter-spacing: 4px;
    opacity: .9;
  }

  /* Front of card */
  .card-front {
    left: 560px;
    top: 430px;
    background: linear-gradient(160deg, var(--white) 0%, var(--paper) 55%, var(--paper-shade) 100%);
  }
  .card-front .wordmark {
    position: absolute;
    left: 40px;
    top: 34px;
    color: var(--blue-deep);
    font-weight: 700;
    font-size: 44px;
    line-height: 1;
  }
  .holder {
    position: absolute;
    right: 36px;
    top: 118px;
    text-align: right;
    width: 220px;
    border-bottom: 1px solid var(--rule);
    padding-bottom: 3px;
  }
  .holder .name { color: var(--red); font-weight: 700; font-size: 18px; line-height: 1.2; }
  .holder .role { color: var(--ink); font-size: 14px; }
  .divider {
    position: absolute;
    left: 40px; right: 36px;
    top: 172px;
    border-top: 1px solid var(--rule);
  }
  .address {
    position: absolute;
    left: 40px;
    top: 182px;
    color: var(--ink);
    font-size: 14px;
  }
  .contacts {
    position: absolute;
    left: 40px;
    top: 210px;
    display: grid;
    grid-template-columns: 170px 220px;
    row-gap: 8px;
    color: var(--ink);
    font-size: 14px;
  }
  .contact { display: flex; align-items: center; gap: 8px; }
  .contact svg { width: 18px; height: 18px; flex: none; }
  .band-red {
    position: absolute;
    left: 0; right: 0;
    bottom: 28px;
    height: 2px;
    background: var(--red);
  }
  .band-blue {
    position: absolute;
    left: 0; right: 0;
    bottom: 0;
    height: 24px;
    background: linear-gradient(90deg, var(--blue-deep) 0%, var(--blue-light) 50%, var(--blue-deep) 100%);
  }

  /* Standalone wordmark */
  .lockup {
    position: absolute;
    left: 50px;
    top: 720px;
    color: var(--white);
    font-weight: 700;
    font-size: 60px;
    line-height: 1;
  }
</style>
</head>
<body>

  <section class="card card-back">
    <div class="wordmark">TMV CA Ltd.</div>
    <div class="web">www.tmvca.com.au</div>
  </section>

  <section class="card card-front">
    <div class="wordmark">TMV CA Ltd.</div>

    <div class="holder">
      <div class="name">Mara Ellison</div>
      <div class="role">Chartered Accountant</div>
    </div>

    <div class="divider"></div>
    <div class="address">42 Harbour Lane, Eastvale, PO Box 3150</div>

    <div class="contacts">
      <div class="contact">
        <svg viewBox="0 0 18 18" aria-hidden="true"><rect width="18" height="18" rx="3" fill="#e6e6e6"/><path d="M5 5c0 5 3 8 8 8l1-2-2-1-1 1c-2-1-3-2-4-4l1-1-1-2z" fill="#c8202f"/></svg>
        <span>(07) 5550 1182</span>
      </div>
      <div class="contact">
        <svg viewBox="0 0 18 18" aria-hidden="true"><rect width="18" height="18" rx="3" fill="#e6e6e6"/><text x="9" y="13" text-anchor="middle" font-size="11" font-weight="700" fill="#c8202f" font-family="Open Sans, sans-serif">@</text></svg>
        <span>info@tmvca.com.au</span>
      </div>
      <div class="contact">
        <svg viewBox="0 0 18 18" aria-hidden="true"><rect width="18" height="18" rx="3" fill="#e6e6e6"/><rect x="6" y="3.5" width="6" height="4" fill="none" stroke="#c8202f" stroke-width="1.2"/><rect x="4" y="7.5" width="10" height="5" rx="1" fill="#c8202f"/><rect x="6" y="11" width="6" height="3.5" fill="#fff" stroke="#c8202f" stroke-width="1"/></svg>
        <span>(07) 5550 1183</span>
      </div>
      <div class="contact">
        <svg viewBox="0 0 18 18" aria-hidden="true"><rect width="18" height="18" rx="3" fill="#e6e6e6"/><circle cx="9" cy="9" r="5" fill="none" stroke="#c8202f" stroke-width="1.3"/><ellipse cx="9" cy="9" rx="2.2" ry="5" fill="none" stroke="#c8202f" stroke-width="1"/><line x1="4" y1="9" x2="14" y2="9" stroke="#c8202f" stroke-width="1"/></svg>
        <span>www.tmvca.com.au</span>
      </div>
    </div>

    <div class="band-red"></div>
    <div class="band-blue"></div>
  </section>

  <div class="lockup">TMV CA Ltd.</div>

</body>
</html>
```